wooden jewelry - pearl necklaces

I sell wooden jeweler (rings and pearls) on markets, and so on. I also opened my business as a carpenter. The rings and a combination of wood and metal. The wood is special wood, not very common on Europe. I paint the rings afterwards. You can see some of the pictures on the pictures I uploaded. The pearls are made of the same kind of wood and colored in all kinds of colors. They are then assembled to bracelets. The jewelry is very individual and looks really cool and all kinds of people.

Target Market(s)

Young urban alternative with a sense of individuality

Contact Information for Business Card

Front:

Text:

„Kugelwerk“ (big)
„Malte Oswitz“ (smaler)

Back
„Holzschmuck
Herstellung von individuellem Holz- und Modeschmuck

Malte Oswitz
Tel: 015239460518
Lindgarbweg 9
83127 Burghausen

malteoswitz@postfeld.de“

Font styles to use
Sans Serif

Requirements
Nice to have
• Nice to see a camel thorn tree on the background, this is a special wood and some of the rings are made out of this wood.

```html
<!DOCTYPE html>
<html lang="de">
<head>
<meta charset="utf-8">
<title>Kugelwerk – Visitenkarte Vorder- und Rückseite</title>
<link rel="stylesheet" href="https://fonts.googleapis.com/css2?family=Bebas+Neue&family=Work+Sans:wght@400&display=swap">
<style>
  :root {
    --backdrop: #1c1c1c;
    --card-paper: #efefee;
    --ink: #3a3a3a;
    --rule: #4a4a4a;
    --light-text: #ffffff;
    --bead-dark: #2a1a1c;
    --bead-brown: #6b3a25;
    --bead-tan: #c9a86a;
    --bead-cream: #e3d2a4;
  }
  html, body {
    margin: 0;
    padding: 0;
    width: 1200px;
    height: 897px;
    overflow: hidden;
    background: var(--backdrop);
  }
  .canvas {
    position: relative;
    width: 1200px;
    height: 897px;
  }
  .card {
    position: absolute;
    left: 326px;
    width: 543px;
    height: 310px;
    box-shadow: 0 10px 18px rgba(0,0,0,0.55);
    overflow: hidden;
  }
  .card--front {
    top: 127px;
    background: var(--card-paper);
  }
  .card--back {
    top: 475px;
  }
  .identity {
    position: absolute;
    right: 300px;
    top: 131px;
    text-align: right;
  }
  .identity__name {
    margin: 0;
    font-family: "Bebas Neue", sans-serif;
    font-weight: 400;
    font-size: 36px;
    line-height: 32px;
    letter-spacing: 2px;
    color: var(--ink);
  }
  .identity__role {
    margin: 4px 0 0;
    font-family: "Work Sans", sans-serif;
    font-size: 13px;
    line-height: 16px;
    color: var(--ink);
  }
  .divider {
    position: absolute;
    left: 269px;
    top: 122px;
    width: 1px;
    height: 66px;
    background: var(--rule);
  }
  .contact {
    position: absolute;
    left: 290px;
    top: 116px;
    margin: 0;
    font-family: "Work Sans", sans-serif;
    font-size: 13.5px;
    line-height: 19.5px;
    letter-spacing: 0.8px;
    color: var(--ink);
  }
  .bead-photo {
    position: absolute;
    inset: 0;
    background:
      radial-gradient(circle at 20% 30%, var(--bead-cream) 0, transparent 30%),
      radial-gradient(circle at 75% 65%, var(--bead-tan) 0, transparent 35%),
      radial-gradient(circle at 50% 50%, var(--bead-brown) 0, transparent 60%),
      linear-gradient(135deg, var(--bead-brown), var(--bead-dark) 55%, var(--bead-brown));
  }
  .brand-name {
    position: absolute;
    left: 0;
    right: 0;
    top: 141px;
    margin: 0;
    text-align: center;
    font-family: "Work Sans", sans-serif;
    font-weight: 400;
    font-size: 22px;
    line-height: 26px;
    letter-spacing: 2px;
    color: var(--light-text);
  }
</style>
</head>
<body>
  <main class="canvas">
    <section class="card card--front">
      <div class="identity">
        <h1 class="identity__name">Malte Oswitz</h1>
        <p class="identity__role">Holzschmuck</p>
      </div>
      <div class="divider"></div>
      <p class="contact">
        015239460518<br>
        malteoswitz@postfeld.de<br>
        Lindgarbweg 9<br>
        83127 Burghausen
      </p>
    </section>
    <section class="card card--back">
      <div class="bead-photo" role="img" aria-label="Foto vieler bunter Holzperlen in Creme, Hellbraun, Rot und Dunkelbraun"></div>
      <p class="brand-name">Kugelwerk</p>
    </section>
  </main>
</body>
</html>
```